Help our Velvet Parlour find our winning design! We're looking for a business card....

We’re a Velvet Parlour in NY specializing in custom-made cakes and unique desserts.
Our cakes combine flavor and art, each designed to match customer’s special event and theme.
We’d like a unique business card with a clean design that will combine French chic and artistic look & feel.
We’d like to differentiate ourselves from standard bakeries, please don’t offer cupcake images :-)
Our logo is peach-pink and brown and we’d love to use these colors ( . Another color that can be added is gold - or feel free to suggest!

Target Market(s)

Women, ages 25-55

Industry/Entity Type

Boutique

Contact Information for Business Card

Text on card:
Logo
Velvet Parlour by Nadia Fenwick

www.xxxxxxxx.com
xxx@xxxxx.com
(555) xxx-xxxx
F – xxxxxxxxxx
IG - xxxxxxxxx

Font styles to use
Sans Serif
Script

Requirements
Must have
• Logo
• Clean look
• French chic and artistic look & feel.
Nice to have
• Damask pattern
Should not have
• Cupcake images

```html
<!DOCTYPE html>
<html lang="en">
<head>
<meta charset="utf-8">
<title>Velvet Parlour – Business Card</title>
<link rel="stylesheet" href="https://fonts.googleapis.com/css2?family=Exo+2:wght@400;600&family=Great+Vibes&display=swap">
<style>
  :root {
    --backdrop: #e9e6e3;
    --paper: #ffffff;
    --ink: #4a4646;
    --ink-soft: #6d6868;
    --rule: #8a8585;
    --blush: #f08a9c;
    --taupe: #6e6866;
  }
  * { box-sizing: border-box; margin: 0; padding: 0; }
  html, body { width: 1200px; height: 800px; overflow: hidden; }
  body {
    background: var(--backdrop);
    font-family: "Exo 2", sans-serif;
    color: var(--ink);
    position: relative;
  }
  .card {
    position: absolute;
    top: 120px;
    width: 320px;
    height: 560px;
    background: var(--paper);
    box-shadow: 0 8px 24px rgba(0,0,0,.18);
    overflow: hidden;
  }
  .card--front { left: 230px; }
  .card--back { left: 650px; }

  .corner-fold { position: absolute; top: 0; left: 0; }

  .wordmark {
    position: absolute;
    left: 0; right: 0;
    text-align: center;
    font-family: "Great Vibes", cursive;
    color: var(--ink);
    font-size: 40px;
    line-height: 1;
  }
  .card--front .wordmark { top: 120px; }
  .card--back .wordmark { top: 130px; }

  .identity { position: absolute; top: 215px; left: 40px; right: 40px; text-align: center; }
  .identity__name { font-size: 22px; font-weight: 600; letter-spacing: .08em; text-transform: uppercase; }
  .identity__role { font-size: 14px; color: var(--ink-soft); margin-top: 4px; }

  .contacts { position: absolute; top: 300px; left: 40px; right: 40px; list-style: none; }
  .contacts__item {
    display: flex; align-items: center; gap: 10px;
    font-size: 11px; color: var(--ink-soft);
    padding: 8px 0 6px;
    border-bottom: 1px solid var(--rule);
  }
  .contacts__item svg { flex: none; }

  .divider { position: absolute; left: 0; top: 0; }

  .web {
    position: absolute; bottom: 60px; left: 0; right: 0;
    text-align: center;
    font-size: 14px; letter-spacing: .14em; color: var(--ink-soft);
  }
</style>
</head>
<body>

<article class="card card--front">
  <svg class="corner-fold" width="90" height="110" viewBox="0 0 90 110">
    <polygon points="0,0 90,0 0,110" fill="var(--taupe)"/>
    <polygon points="30,0 90,0 10,95" fill="var(--blush)"/>
  </svg>

  <div class="wordmark">Velvet Parlour</div>

  <header class="identity">
    <h1 class="identity__name">Nadia Fenwick</h1>
    <p class="identity__role">Managing Director</p>
  </header>

  <ul class="contacts">
    <li class="contacts__item">
      <svg width="12" height="12" viewBox="0 0 24 24"><path d="M6.6 10.8a15 15 0 0 0 6.6 6.6l2.2-2.2c.3-.3.7-.4 1-.2 1.1.4 2.3.6 3.6.6.6 0 1 .4 1 1V20c0 .6-.4 1-1 1A17 17 0 0 1 3 4c0-.6.4-1 1-1h3.5c.6 0 1 .4 1 1 0 1.3.2 2.5.6 3.6.1.3 0 .7-.2 1z" fill="var(--ink)"/></svg>
      (555) xxx-xxxx
    </li>
    <li class="contacts__item">
      <svg width="12" height="12" viewBox="0 0 24 24"><rect x="2" y="5" width="20" height="14" rx="1" fill="var(--ink)"/><path d="M3 6l9 7 9-7" stroke="#fff" stroke-width="1.6" fill="none"/></svg>
      hello@velvetparlour.com
    </li>
    <li class="contacts__item">
      <svg width="12" height="12" viewBox="0 0 24 24"><circle cx="12" cy="12" r="9" fill="none" stroke="var(--ink)" stroke-width="2"/><path d="M3 12h18M12 3c3 3 3 15 0 18M12 3c-3 3-3 15 0 18" stroke="var(--ink)" stroke-width="1.5" fill="none"/></svg>
      www.velvetparlour.com
    </li>
    <li class="contacts__item">
      <svg width="12" height="12" viewBox="0 0 24 24"><path d="M12 2a7 7 0 0 0-7 7c0 5 7 13 7 13s7-8 7-13a7 7 0 0 0-7-7z" fill="var(--ink)"/><circle cx="12" cy="9" r="2.5" fill="#fff"/></svg>
      48 Bleecker Street, New York NY
    </li>
  </ul>
</article>

<article class="card card--back">
  <div class="wordmark">Velvet Parlour</div>
  <svg class="divider" width="320" height="560" viewBox="0 0 320 560">
    <line x1="10" y1="255" x2="300" y2="390" stroke="var(--rule)" stroke-width="1.2"/>
  </svg>
  <p class="web">www.velvetparlour.com</p>
</article>

</body>
</html>
```